Real Estate Business card design

Company Name: Tamarind Holdings, LLC
subtitle: We pay cash for houses!
Daniel Whitcombe
Managing Director
555-214-0963
Dan@TamarindHoldingsLLC.example
www.TamarindHoldingsLLC.example

We pay referral fees for Seller and Buyer leads.

Back:
We offer referral fees for Seller and Buyer leads that close.

Please contact Hal at 555-214-0963 with your referrals or to learn more about the referral program!

I am open to different color options but I am going for a classic, elegant, clean, and professional look. Please use logo as a reference.

Target Market(s)

People selling their homes and people in the market for buying homes.

Contact Information for Business Card

please see project description

Font styles to use
Serif
Sans Serif
Script

Requirements
Must have
• must have my logo in it
Nice to have
• I like cards that are split down the middle but please come up with a few mock ups. Open to any color scheme.

```html
<!DOCTYPE html>
<html lang="en">
<head>
<meta charset="utf-8">
<title>Tamarind Holdings, LLC – Business Card</title>
<link rel="stylesheet" href="https://fonts.googleapis.com/css2?family=Lato:wght@700&family=Poppins:wght@400;600;700&family=Roboto+Condensed:wght@400;700&display=swap">
<style>
  :root {
    --backdrop: #2a2a2a;
    --card-top: #f4f4f4;
    --card-bottom: #e4e4e4;
    --ink: #3a3d42;
    --ink-soft: #4a4d52;
    --gold-light: #cfa987;
    --gold: #b88f6c;
    --gold-dark: #a07a58;
  }
  * { margin: 0; padding: 0; box-sizing: border-box; }
  html, body { width: 1200px; height: 1138px; overflow: hidden; }
  body { background: var(--backdrop); position: relative; font-family: "Lato", sans-serif; }

  .card {
    position: absolute;
    border-radius: 16px;
    background: linear-gradient(180deg, var(--card-top), var(--card-bottom));
    overflow: hidden;
  }

  /* Front / referral side */
  .card--referral { left: 274px; top: 186px; width: 623px; height: 376px; }
  .referral__brand {
    position: absolute; left: 0; right: 0; top: 120px;
    text-align: center; font-family: "Lato", sans-serif; font-weight: 700;
    font-size: 28px; color: var(--gold);
  }
  .referral__offer {
    position: absolute; left: 0; right: 0; top: 198px;
    text-align: center; font-weight: 700; font-size: 24px; color: var(--ink);
  }
  .referral__rule {
    position: absolute; left: 131px; width: 360px; top: 231px; height: 2px;
    background: var(--gold);
  }
  .referral__contact {
    position: absolute; left: 0; right: 0; top: 236px;
    text-align: center; font-weight: 700; font-size: 24px; color: var(--ink);
  }

  /* Contact side */
  .card--contact { left: 276px; top: 608px; width: 618px; height: 374px; }
  .contact__tab {
    position: absolute; left: -50px; top: 120px; width: 60px; height: 60px;
    border-radius: 50%; background: var(--gold);
  }
  .contact__name {
    position: absolute; left: 39px; top: 122px;
    font-family: "Poppins", sans-serif; font-weight: 700; font-size: 22px; color: var(--ink);
  }
  .contact__title {
    position: absolute; left: 39px; top: 152px;
    font-family: "Poppins", sans-serif; font-weight: 400; font-size: 15px; color: var(--ink-soft);
  }
  .contact__brand {
    position: absolute; right: 38px; top: 110px; text-align: center;
    font-family: "Poppins", sans-serif; font-weight: 600; color: var(--ink); line-height: 1;
  }
  .contact__brand-main { display: block; font-size: 42px; }
  .contact__brand-sub { display: block; font-size: 19px; margin-top: 6px; letter-spacing: 1px; }

  .contact__details {
    position: absolute; left: 40px; top: 278px; list-style: none;
    font-family: "Roboto Condensed", sans-serif; font-size: 15px; color: var(--ink);
  }
  .contact__details li { display: flex; align-items: center; height: 20px; }
  .contact__details svg { width: 11px; height: 11px; margin-right: 10px; fill: var(--gold); }

  .contact__band {
    position: absolute; left: 321px; top: 290px; width: 297px; height: 46px;
    background: linear-gradient(90deg, var(--gold-dark), var(--gold-light) 60%, var(--gold));
    clip-path: polygon(8% 0, 100% 0, 100% 100%, 0 100%);
    display: flex; align-items: center; justify-content: flex-end; padding-right: 38px;
    font-family: "Roboto Condensed", sans-serif; font-weight: 700; font-size: 14px;
    color: #1f1f1f; letter-spacing: 0.3px;
  }
</style>
</head>
<body>

<section class="card card--referral">
  <div class="referral__brand">Tamarind Holdings, LLC</div>
  <p class="referral__offer">We offer referral fees for Seller &amp; Buyer</p>
  <div class="referral__rule"></div>
  <p class="referral__contact">Contact Hal: 555-214-0963</p>
</section>

<section class="card card--contact">
  <div class="contact__tab"></div>
  <h1 class="contact__name">Daniel Whitcombe</h1>
  <p class="contact__title">Managing Director</p>

  <div class="contact__brand">
    <span class="contact__brand-main">Tamarind</span>
    <span class="contact__brand-sub">Holdings, LLC</span>
  </div>

  <ul class="contact__details">
    <li>
      <svg viewBox="0 0 12 12" aria-hidden="true"><path d="M1 3c0-1 1-2 2-2h6c1 0 2 1 2 2v1H8V3H4v1H1z M3 5h6l2 6H1z"/></svg>
      555-214-0963
    </li>
    <li>
      <svg viewBox="0 0 12 12" aria-hidden="true"><path d="M0 2h12v8H0z M0 2l6 5 6-5" stroke="#e8e8e8" stroke-width="1"/></svg>
      Dan@TamarindHoldingsLLC.example
    </li>
    <li>
      <svg viewBox="0 0 12 12" aria-hidden="true"><circle cx="6" cy="6" r="5.5"/><path d="M0.5 6h11M6 0.5v11M2 3h8M2 9h8" stroke="#e8e8e8" stroke-width="0.8" fill="none"/></svg>
      www.TamarindHoldingsLLC.example
    </li>
  </ul>

  <div class="contact__band">WE PAY CASH FOR HOUSES!</div>
</section>

</body>
</html>
```